Need a new company business card

I am looking for a new company business card. Front and back. With information on it as per below. Card should be professional. Yet clever. Simple. Modern design. ZEP card, traditional size. OK with say, all black or all red backside.

Vornadel is an indie, bootstrapped magazine advancing the work of intersectional feminists busting their buts to create a just world through the power of enterprise and innovation.

Vornadel is the home and voice of entrepreneurial feminism and feminist innovators worldwide. Entrepreneurial feminists are people (of all genders) who see inequality as an innovation priority. They work to advance gender equity and/or who strive to integrate and practice feminist principles, pedagogy, values into their innovation and entrepreneurship work.
We are committed to this space being trans and queer inclusive, anti-racist, intersectional, brave, and safe. We welcome all allies. We value learning, edgy but civil discourse and integrative thinking skills.

Target Market(s)

feminists, business owners,

Industry/Entity Type

Publishing Company

Contact Information for Business Card

TJ Harlow
Founder/Publisher
4-237 Pellridge Street, Toronto, ON
M4T 2K8
publisher@vornadel-example.com
416-555-3042
www.vornadel-example.com

Font styles to use
Serif
Other font styles liked:
• Myriad Pro

Colors
ec1f27
000000
ffffff

Requirements
Must have
• logo
• use red, black white colours only.
Nice to have
• use the compass in pattern or creatively but not too busy please
Should not have
• Should not be too busy. Elegant.

```html
<!DOCTYPE html>
<html lang="en">
<head>
<meta charset="utf-8">
<title>Vornadel business card</title>
<link rel="stylesheet" href="https://fonts.googleapis.com/css2?family=Open+Sans:wght@400;700;800&display=swap">
<style>
  :root {
    --page: #ececec;
    --card-white: #f1f1f1;
    --card-black: #2b2b2b;
    --ink: #2e2e2e;
    --ink-soft: #4a4a4a;
    --red: #d7262e;
    --rule: #9c9c9c;
    --pattern: #a9a9a9;
    --white: #ffffff;
  }
  * { box-sizing: border-box; margin: 0; padding: 0; }
  html, body { width: 1200px; height: 1176px; overflow: hidden; }
  body {
    background: var(--page);
    font-family: "Open Sans", Arial, sans-serif;
    display: flex;
    flex-direction: column;
    align-items: center;
    justify-content: center;
    gap: 48px;
  }
  .card {
    width: 900px;
    height: 514px;
    position: relative;
    box-shadow: 0 6px 18px rgba(0,0,0,.12);
  }

  /* Front */
  .card-front { background: var(--card-white); }
  .border-pattern {
    position: absolute; inset: 0;
    background: var(--pattern);
  }
  .front-panel {
    position: absolute; inset: 34px;
    background: var(--card-white);
    display: flex;
    align-items: center;
  }
  .front-brand {
    width: 50%;
    display: flex;
    justify-content: center;
  }
  .divider {
    width: 1px; height: 200px;
    background: var(--rule);
  }
  .contact {
    width: 50%;
    padding-left: 42px;
    color: var(--ink-soft);
    font-size: 19px;
    line-height: 1.35;
  }
  .contact-name {
    font-size: 30px; font-weight: 800; color: var(--ink);
    line-height: 1.1;
  }
  .contact-title { margin-bottom: 10px; }
  .contact-lines { list-style: none; margin-top: 10px; }
  .contact-lines li { display: flex; align-items: center; gap: 10px; }
  .contact-lines svg { width: 18px; height: 18px; flex: none; }

  /* Brand name */
  .brand { display: inline-flex; align-items: center; gap: 10px; }
  .brand-name {
    font-weight: 800;
    font-size: 58px;
    line-height: 1;
    letter-spacing: -1px;
    color: var(--ink);
  }
  .cert-badge {
    width: 18px; height: 18px;
    border: 1.5px solid var(--ink-soft);
    border-radius: 50%;
  }

  /* Back */
  .card-back {
    background: var(--card-black);
    display: flex; align-items: center; justify-content: center;
  }
  .back-lockup { display: flex; align-items: center; gap: 26px; }
  .back-dot {
    width: 92px; height: 92px; border-radius: 50%;
    background: var(--red);
  }
  .card-back .brand-name { color: var(--white); font-size: 78px; }
</style>
</head>
<body>

  <section class="card card-front" aria-label="Business card front">
    <div class="border-pattern" role="img" aria-label="Grey striped decorative pattern framing the card"></div>
    <div class="front-panel">
      <div class="front-brand">
        <div class="brand">
          <span class="brand-name">Vornadel</span>
          <span class="cert-badge" aria-hidden="true"></span>
        </div>
      </div>
      <div class="divider"></div>
      <div class="contact">
        <p class="contact-name">TJ Harlow</p>
        <p class="contact-title">Founder/Publisher</p>
        <p>4-237 Pellridge Street<br>Toronto, ON, M4T 2K8</p>
        <ul class="contact-lines">
          <li>
            <svg viewBox="0 0 24 24" aria-hidden="true"><path fill="#d7262e" d="M6.6 10.8a15 15 0 0 0 6.6 6.6l2.2-2.2a1 1 0 0 1 1-.25 11.4 11.4 0 0 0 3.6.57 1 1 0 0 1 1 1V20a1 1 0 0 1-1 1A17 17 0 0 1 3 4a1 1 0 0 1 1-1h3.5a1 1 0 0 1 1 1c0 1.25.2 2.45.57 3.57a1 1 0 0 1-.25 1z"/></svg>
            416-555-3042
          </li>
          <li>
            <svg viewBox="0 0 24 24" aria-hidden="true"><rect x="3" y="5" width="18" height="14" fill="none" stroke="#d7262e" stroke-width="2"/><path d="M3 5l9 7 9-7" fill="none" stroke="#d7262e" stroke-width="2"/></svg>
            publisher@vornadel-example.com
          </li>
          <li>
            <svg viewBox="0 0 24 24" aria-hidden="true"><g fill="none" stroke="#d7262e" stroke-width="1.8"><circle cx="12" cy="12" r="9"/><ellipse cx="12" cy="12" rx="4" ry="9"/><path d="M3 12h18M5 7h14M5 17h14"/></g></svg>
            www.vornadel-example.com
          </li>
        </ul>
      </div>
    </div>
  </section>

  <section class="card card-back" aria-label="Business card back">
    <div class="back-lockup">
      <span class="back-dot" aria-hidden="true"></span>
      <span class="brand-name">Vornadel</span>
    </div>
  </section>

</body>
</html>
```